Domestic Building Company requires professional webpage

We have an existing webpage that was never completed. We are a growing building company specialising in domestic building, renovations and commercial maintenance. We liaise closely with each of our clients to provide quality service they would be happy to recommend. Our easy approachable staff give our clients the confidence to discuss their needs and changes they may have along the way.
Our main source of new customers have been from recommendations of existing clients.
We would like our webpage to reflect our eye for detail and showcase our previous work.
The colour theme should be the same as the colours of our logo.
We would like the main page to really stand out with a slideshow of our pictures of works we have completed.
We would like the tabs to remain the same - Home, About Us, Our Services, Contact us.
In the Our Services section we would like each sub heading to be a link where viewers can see pictures from previous work we have completed.
Our current web page is www.ferncastconstruct.com.au

```html
<!DOCTYPE html>
<html lang="en">
<head>
<meta charset="utf-8">
<title>Ferncast Construct – Home</title>
<link rel="stylesheet" href="https://fonts.googleapis.com/css2?family=Open+Sans:wght@300;400;600&display=swap">
<style>
:root{
  --green:#8cc63f;
  --green-dark:#5fa52e;
  --blue:#0b57a4;
  --blue-deep:#0a3f8a;
  --text:#666;
  --text-dark:#333;
  --rule:#e2e2e2;
  --footer-top:#1a6bbd;
  --footer-bottom:#0a3c8e;
}
*{box-sizing:border-box;margin:0;padding:0}
html,body{width:1042px;height:1200px;overflow:hidden;background:#fff}
body{font-family:"Open Sans",Arial,sans-serif;color:var(--text);position:relative}
.abs{position:absolute}

/* header */
.site-header{position:absolute;left:0;top:0;width:1042px;height:118px;border-bottom:1px solid #ddd;background:#fff}
.brand{position:absolute;left:75px;top:36px;display:flex;align-items:center;gap:12px}
.brand-mark{width:36px;height:36px;background:var(--green)}
.brand-name{font-size:30px;font-weight:600;color:var(--blue);letter-spacing:-.5px;line-height:1}
.social{position:absolute;top:32px;left:835px;display:flex;gap:9px}
.social a{display:block;width:24px;height:24px;border-radius:3px}
.social .s1{background:#3b5998}.social .s2{background:#4cc2ee}.social .s3{background:#1b76b5}.social .s4{background:#f7931d}
.main-nav{position:absolute;top:75px;left:0;width:1042px;height:20px}
.main-nav a{position:absolute;font-size:15px;font-weight:600;color:var(--blue);text-decoration:none;white-space:nowrap}
.main-nav a.active{color:var(--green)}
.nav-indicator{position:absolute;left:420px;top:112px;width:54px;height:5px;background:var(--green)}

/* hero */
.hero{position:absolute;left:0;top:118px;width:1042px;height:385px;
  background:linear-gradient(180deg,#6f7a55 0%,#8a6a4c 35%,#7d5a3e 60%,#5f6b3a 80%,#6f8a3c 100%)}
.hero-title{position:absolute;left:77px;top:100px;font-size:37px;color:#fff;font-weight:400;text-shadow:0 1px 3px rgba(0,0,0,.5);letter-spacing:.5px}
.hero-sub{position:absolute;left:77px;top:142px;font-size:28px;color:#fff;text-shadow:0 1px 3px rgba(0,0,0,.5)}
.hero-text{position:absolute;left:78px;top:182px;font-size:12.5px;line-height:20px;color:#fff;text-shadow:0 1px 2px rgba(0,0,0,.6)}
.hero-dots{position:absolute;left:78px;top:238px;display:flex;gap:4px}
.hero-dots span{width:13px;height:13px;border-radius:50%;background:rgba(255,255,255,.35)}
.hero-dots span.on{background:#fff}

/* welcome */
.welcome-title{left:74px;top:543px;font-size:26px;color:var(--blue-deep);font-weight:400}
.welcome-sub{left:74px;top:574px;font-size:16px;color:var(--blue);font-weight:400}
.welcome-copy{left:71px;top:604px;width:560px;font-size:11.5px;line-height:19.3px}
.welcome-copy p+p{margin-top:9px}
.btn{position:absolute;display:flex;align-items:center;justify-content:center;color:#fff;font-size:12.5px;font-weight:600;border-radius:3px;text-decoration:none;text-shadow:0 1px 1px rgba(0,0,0,.3)}
.btn-blue{left:72px;top:743px;width:109px;height:32px;background:linear-gradient(#1e74c9,#0b4c9c)}
.btn-green{left:408px;top:1023px;width:109px;height:31px;background:linear-gradient(#8dcc4f,#4f9c2a)}

/* old projects */
.old-projects{position:absolute;left:653px;top:543px;width:307px;height:237px;border-radius:3px;
  background:linear-gradient(#a3d66b,#5ea72f)}
.old-projects h2{position:absolute;left:23px;top:16px;font-size:24px;font-weight:400;color:#fff}
.thumb{position:absolute;width:86px;height:72px;border:2px solid #fff;border-radius:4px}
.t1{background:linear-gradient(135deg,#3d3a36,#8a8780)}
.t2{background:linear-gradient(#7a6a52,#5e7c3a)}
.t3{background:linear-gradient(90deg,#8e9091,#4fc1b0)}
.t4{background:linear-gradient(135deg,#2e2620,#9a8a78)}
.t5{background:linear-gradient(#7c8f74,#4d4d4a)}
.t6{background:linear-gradient(#6d6a67,#2a3a6a)}

/* columns */
.col-title{top:814px;font-size:21px;font-weight:400;color:#333}
.col-title.blue{color:var(--blue-deep)}
.project{position:absolute;left:76px;width:300px;height:60px}
.project .pic{position:absolute;left:0;top:0;width:74px;height:57px}
.project h3{position:absolute;left:84px;top:-1px;font-size:13.5px;font-weight:400;color:#333}
.project p{position:absolute;left:84px;top:20px;width:215px;font-size:11px;line-height:16px;color:#888}
.why-copy{left:407px;top:849px;width:275px;font-size:11.5px;line-height:19.3px}
.why-copy p+p{margin-top:9px}
.services{position:absolute;left:706px;top:847px;width:255px;list-style:none}
.services li{height:30.7px;display:flex;align-items:center;gap:9px;font-size:11.5px;color:#555;border-bottom:1px solid #eee}
.services li:last-child{border-bottom:none}
.services svg{flex:none}

/* footer */
.site-footer{position:absolute;left:0;top:1103px;width:1042px;height:97px;background:linear-gradient(var(--footer-top),var(--footer-bottom))}
.footer-nav{position:absolute;left:78px;top:23px;font-size:14px;color:#fff;white-space:nowrap}
.footer-nav a{color:#fff;text-decoration:none}
.footer-nav span{margin:0 8px}
.copyright{position:absolute;left:78px;top:50px;font-size:11.5px;color:#7ea6d8}
</style>
</head>
<body>

<header class="site-header">
  <div class="brand"><span class="brand-mark"></span><span class="brand-name">ferncast construct</span></div>
  <div class="social">
    <a class="s1" href="#" aria-label="Social link"></a>
    <a class="s2" href="#" aria-label="Social link"></a>
    <a class="s3" href="#" aria-label="Social link"></a>
    <a class="s4" href="#" aria-label="Feed"></a>
  </div>
  <nav class="main-nav">
    <a class="active" href="#" style="left:424px">HOME</a>
    <a href="#" style="left:496px">ABOUT US</a>
    <a href="#" style="left:598px">OUR SERVICES</a>
    <a href="#" style="left:734px">OUR PROJECTS</a>
    <a href="#" style="left:869px">CONTACT US</a>
  </nav>
  <span class="nav-indicator"></span>
</header>

<section class="hero" role="img" aria-label="Photo of a timber gazebo on a wooden deck in a garden">
  <h1 class="hero-title">Construction &amp; Building</h1>
  <p class="hero-sub">Phasellus felis dolor scelerisque</p>
  <p class="hero-text">Morbi diam mauris viverra in gravida eu mattis in ante Morbi eget arcu<br>Morbi porta libero id ullamcorper nonummy nibh ligula pulvinar</p>
  <div class="hero-dots"><span class="on"></span><span></span><span></span><span></span></div>
</section>

<h2 class="abs welcome-title">Welcome to Our Website Mainpage</h2>
<p class="abs welcome-sub">Mauris nunc quam venenatis nec euismod sit amet&nbsp; egestas placerat est</p>
<div class="abs welcome-copy">
  <p>Ferncast Construct Pty Ltd is a construction and renovation company that is based in the Illawarra area.&nbsp; We specialise in all areas of residential and commercial building works and aim to deliver the highest quality performance at an affordable price. We ensure our workers have undergone the qualifications and training to provide the workmanship, efficiency and reliability our clients expect.</p>
  <p>We actively engage our client from the initial greeting to the finished product, we achieve this by ensuring the clients needs remain our first priority when delivering a high quality service and product.</p>
</div>
<a class="btn btn-blue" href="#">READ MORE</a>

<aside class="old-projects">
  <h2>Old Projects</h2>
  <div class="thumb t1" style="left:22px;top:54px" role="img" aria-label="Project photo: interior stairs"></div>
  <div class="thumb t2" style="left:113px;top:54px" role="img" aria-label="Project photo: garden gazebo"></div>
  <div class="thumb t3" style="left:204px;top:54px" role="img" aria-label="Project photo: rendered exterior with teal door"></div>
  <div class="thumb t4" style="left:22px;top:134px" role="img" aria-label="Project photo: interior hallway"></div>
  <div class="thumb t5" style="left:113px;top:134px" role="img" aria-label="Project photo: slatted screen fence"></div>
  <div class="thumb t6" style="left:204px;top:134px" role="img" aria-label="Project photo: finished bedroom"></div>
</aside>

<h2 class="abs col-title" style="left:76px">Latest Projects</h2>
<div class="project" style="top:853px">
  <div class="pic" role="img" aria-label="Photo of a renovated living room" style="background:linear-gradient(#8a7a6a,#3e3a38)"></div>
  <h3>Etiam est nunc venenatis</h3>
  <p>Class aptent taciti sociosqu ad litora torquent per conubia nostra, per inceptos</p>
</div>
<div class="project" style="top:926px">
  <div class="pic" role="img" aria-label="Photo of a timber cabinet" style="background:linear-gradient(#5a3e26,#8a6a44)"></div>
  <h3>Mauris neque metus</h3>
  <p>Class aptent taciti sociosqu ad litora torquent per conubia nostra hymenaeos</p>
</div>
<div class="project" style="top:998px">
  <div class="pic" role="img" aria-label="Photo of a tiled bathroom with spa bath" style="background:linear-gradient(#6a6460,#d8dcdc)"></div>
  <h3>Curabitur iaculis</h3>
  <p>Class aptent taciti sociosqu per conubia nostra, per inceptos hymenaeos</p>
</div>

<h2 class="abs col-title" style="left:406px">Why Choose Us</h2>
<div class="abs why-copy">
  <p>Aliquam nec erat at purus cursus interdum Vestibu-lum ligula augue bibendum accumsan vestibulum ut commodo a mi Morbi ornare gravida elit Integer congue augue et malesuada iaculis ipsum dui aliquet felis at cursus magna nisl nec elit</p>
  <p>Vestibulum gravida Praesent elementum elit at tellus Malesuada nec ultricies sit ametporttitor mattis enim In massa libero interdum nec</p>
</div>
<a class="btn btn-green" href="#">READ MORE</a>

<h2 class="abs col-title blue" style="left:706px">Services We Provide</h2>
<ul class="services">
  <li><svg width="5" height="9" viewBox="0 0 5 9"><path d="M0 0 L5 4.5 L0 9Z" fill="#bbb"/></svg>Etiam eu urna Sed porta Suspendisse</li>
  <li><svg width="5" height="9" viewBox="0 0 5 9"><path d="M0 0 L5 4.5 L0 9Z" fill="#bbb"/></svg>Quam leo molestie sed luctus quis feugiat</li>
  <li><svg width="5" height="9" viewBox="0 0 5 9"><path d="M0 0 L5 4.5 L0 9Z" fill="#bbb"/></svg>Fusce tellus Sed metus augue convallis</li>
  <li><svg width="5" height="9" viewBox="0 0 5 9"><path d="M0 0 L5 4.5 L0 9Z" fill="#bbb"/></svg>Et vehicula ut pulvinar eu ante Integer</li>
  <li><svg width="5" height="9" viewBox="0 0 5 9"><path d="M0 0 L5 4.5 L0 9Z" fill="#bbb"/></svg>Eristique vitae consequat nec porta vel lectus</li>
  <li><svg width="5" height="9" viewBox="0 0 5 9"><path d="M0 0 L5 4.5 L0 9Z" fill="#bbb"/></svg>Nulla sit amet diam Duis non nunc</li>
</ul>

<footer class="site-footer">
  <nav class="footer-nav">
    <a href="#">Home</a><span>|</span><a href="#">About us</a><span>|</span><a href="#">Millwork projects</a><span>|</span><a href="#">House designs</a><span>|</span><a href="#">Contact us</a>
  </nav>
  <p class="copyright">Copyright © 2013 Company Name.&nbsp; All right reseved</p>
</footer>

</body>
</html>
```